Wilderness Doc & TV personality personal page

I’m a wilderness and EMS emergency physician with particular sub specialties and a TV show. I need a website to highlight my interviews, teachings, etc... I did buy a number of domains for now.
Topics and things I need: CV (or version) me in the media, picture gallery, actually I sort of really like what dr ned harlow, my colleague has setup plus I have tv show and stuff like that. pinecrest rover dot com

Target Market(s)

EMS, education, commercial products...

Industry/Entity Type

Medical And Science

Coding

Coded - Design and coding required

Number of Pages Required

1 page

Font styles to use
Sans Serif

Colors
f37122
9bcb3c
0556a4
a54499

Requirements
Must have
• Links and photos to news articles and things that mention me that I can add in.
Nice to have
• Maybe some snapshots of lecture reviews or patient thank you notes. Accolades so to speak
• I really appreciate how sharp it is. I would love to see Headings that resemble my friend's at pinecrest rover dot com. Home, experience, consulting, lectures, affiliates, contact... those are main subjects... I think media also and that will have the TV show stuff and articles written about me...then maybe at the bottom of main page also have splits for training, research, television, and maybe exploration
Should not have
• The medical symbol with two snakes... that means quack doctor

```html
<!DOCTYPE html>
<html lang="en">
<head>
<meta charset="utf-8">
<title>Trailside MD – Shows, Interviews and Lectures</title>
<link href="https://fonts.googleapis.com/css2?family=Roboto:wght@300;400;500;700&family=Roboto+Condensed:wght@400;700&display=swap" rel="stylesheet">
<style>
:root{
  --blue:#0556a4;
  --blue-dark:#044886;
  --blue-deep:#033a6e;
  --orange:#f37122;
  --green:#9bcb3c;
  --purple:#a54499;
  --ink:#333;
  --muted:#888;
  --line:#e3e3e3;
  --soft:#f2f2f2;
  --white:#fff;
}
*{box-sizing:border-box;margin:0;padding:0}
html,body{width:1200px;height:2372px;overflow:hidden}
body{font-family:"Roboto",Arial,sans-serif;color:var(--ink);background:var(--white);position:relative;font-size:12px}
h1,h2,h3,h4{font-family:"Roboto Condensed","Roboto",sans-serif;font-weight:700}
.photo{display:block}

/* top bar */
.topbar{position:absolute;top:0;left:0;width:1200px;height:44px;background:var(--blue-dark);display:flex;align-items:center;padding:0 20px}
.brand{display:flex;align-items:center;gap:8px;color:var(--white);font-weight:700;font-size:20px;letter-spacing:.5px}
.brand-dot{width:12px;height:12px;border-radius:50%;background:var(--green)}
.main-nav{display:flex;margin-left:auto;height:44px}
.main-nav a{color:var(--white);text-decoration:none;font-size:12px;padding:0 18px;display:flex;align-items:center}
.main-nav a.is-active{background:var(--orange)}
.top-tools{display:flex;align-items:center;gap:18px;margin-left:30px;color:var(--white)}
.user{display:flex;align-items:center;gap:8px;font-size:11px;line-height:1.2}
.avatar{width:28px;height:28px;border-radius:50%;background:#8aa7c7}

/* hero */
.hero{position:absolute;top:44px;left:0;width:1200px;height:476px}
.hero-stage{position:absolute;left:0;top:0;width:880px;height:476px;background:linear-gradient(135deg,#dfe6ee 0%,#b9c6d3 45%,#56606d 100%)}
.hero-tab{position:absolute;left:0;top:0;background:var(--blue);color:var(--white);font-size:11px;padding:6px 14px}
.hero-caption{position:absolute;left:30px;bottom:48px;color:var(--white)}
.hero-caption h1{font-size:34px;font-weight:400;letter-spacing:1px}
.hero-caption p{font-size:12px;margin-top:4px;opacity:.9}
.hero-dots{position:absolute;left:30px;bottom:24px;display:flex;gap:6px}
.hero-dots span{width:8px;height:8px;border-radius:50%;background:rgba(255,255,255,.5)}
.hero-dots span.on{background:var(--orange)}
.favorites{position:absolute;left:880px;top:0;width:320px;height:476px;background:var(--blue-deep);color:var(--white)}
.favorites h3{font-size:13px;font-weight:400;padding:10px 16px;background:var(--blue)}
.fav-item{display:flex;gap:12px;padding:10px 16px;border-bottom:1px solid rgba(255,255,255,.12)}
.fav-thumb{width:130px;height:66px;background:linear-gradient(135deg,#8fa6bf,#3e5a78);flex:none;position:relative}
.fav-thumb::after{content:"";position:absolute;left:55px;top:23px;width:20px;height:20px;border-radius:50%;background:var(--orange)}
.fav-text b{display:block;font-size:12px;font-weight:500;margin-top:6px}
.fav-text small{font-size:10px;opacity:.7}

/* sidebar */
.sidebar{position:absolute;top:520px;left:0;width:320px;height:640px;background:var(--blue);color:var(--white);padding:24px 0}
.side-menu{list-style:none;padding:0 24px 18px;border-bottom:1px solid rgba(255,255,255,.2)}
.side-menu li{font-size:12px;padding:6px 0}
.side-menu li.head{opacity:.7;font-size:11px}
.side-list{padding:10px 24px}
.side-list .label{font-size:11px;opacity:.7;padding:6px 0}
.side-entry{padding:10px 0;border-bottom:1px solid rgba(255,255,255,.2)}
.side-entry b{display:block;font-size:12px;font-weight:500}
.side-entry p{font-size:10px;opacity:.8;margin-top:3px;line-height:1.4}

/* popular */
.popular{position:absolute;top:520px;left:320px;width:880px;height:640px;padding:40px 20px 0 20px}
.section-head{display:flex;align-items:center;border-bottom:2px solid var(--line);padding-bottom:10px}
.section-head h2{font-size:24px;color:var(--ink);font-weight:400;letter-spacing:.5px}
.section-head h2 b{font-weight:700}
.filter{margin-left:auto;display:flex;align-items:center;gap:12px;font-size:11px;color:var(--muted)}
.filter .select{border:1px solid var(--line);padding:4px 10px}
.grid{display:grid;grid-template-columns:repeat(4,1fr);gap:26px 16px;margin-top:22px}
.card .thumb{height:128px;background:linear-gradient(135deg,#d7dde4,#7b8895);position:relative}
.card .thumb::after{content:"";position:absolute;left:50%;top:50%;width:26px;height:26px;margin:-13px;border-radius:50%;background:rgba(255,255,255,.85)}
.card h4{font-family:"Roboto",sans-serif;font-weight:500;font-size:13px;margin-top:8px}
.card p{font-size:10px;color:var(--muted);margin-top:3px}
.card .meta{display:flex;gap:14px;font-size:10px;color:var(--muted);margin-top:8px}
.card .meta i{font-style:normal;color:var(--orange)}

/* interview */
.interview{position:absolute;top:1160px;left:0;width:1200px;height:440px;background:var(--soft)}
.interview-photo{position:absolute;right:0;top:0;width:760px;height:440px;background:linear-gradient(120deg,#f1f1f1 0%,#cfd5db 35%,#6c7682 100%)}
.interview-copy{position:absolute;left:100px;top:120px;width:330px}
.interview-copy h2{font-size:40px;font-weight:400;color:var(--ink);letter-spacing:1px}
.interview-copy h3{font-size:26px;font-weight:400;color:var(--ink)}
.interview-copy p{font-size:11px;color:var(--muted);line-height:1.5;margin-top:16px}
.btn{display:inline-block;background:var(--orange);color:var(--white);font-size:10px;font-weight:700;padding:8px 16px;margin-top:18px;text-decoration:none}

/* lecture + news */
.lower{position:absolute;top:1640px;left:100px;width:1000px;display:flex;gap:60px}
.lecture{width:620px}
.col-head h2{font-size:26px;font-weight:400;letter-spacing:.5px}
.col-head p{font-size:11px;color:var(--muted);margin-top:2px;padding-bottom:10px;border-bottom:2px solid var(--line)}
.lec-grid{display:grid;grid-template-columns:1fr 1fr;gap:30px 40px;margin-top:20px}
.lec .thumb{height:150px;background:linear-gradient(135deg,#c8cfd8,#5d6b7a)}
.stars{color:var(--orange);font-size:12px;letter-spacing:2px;margin-top:8px}
.lec h4{font-family:"Roboto",sans-serif;font-size:13px;font-weight:500;margin-top:4px}
.lec p{font-size:10px;color:var(--muted);margin-top:4px;line-height:1.4}
.news{width:320px}
.news-item{display:flex;gap:12px;padding:12px 0;border-bottom:1px solid var(--line)}
.news-thumb{width:70px;height:50px;flex:none;background:linear-gradient(135deg,#c8cfd8,#5d6b7a)}
.news-item b{display:block;font-size:12px;font-weight:500}
.news-item p{font-size:10px;color:var(--muted);line-height:1.4;margin-top:3px}

/* footer */
.footer{position:absolute;top:2250px;left:0;width:1200px;height:122px;border-top:1px solid var(--line);text-align:center;padding-top:30px}
.social{display:flex;justify-content:center;gap:14px}
.social span{width:22px;height:22px;border-radius:50%;background:#bbb}
.copy{font-size:10px;color:var(--muted);margin-top:16px}
.copy b{color:var(--orange);font-weight:400}
</style>
</head>
<body>

<header class="topbar">
  <div class="brand"><span class="brand-dot"></span>Trailside MD</div>
  <nav class="main-nav">
    <a href="#">All Shows</a>
    <a href="#" class="is-active">Exposure</a>
    <a href="#">Lectures</a>
    <a href="#">Blog</a>
    <a href="#">Contact Us</a>
  </nav>
  <div class="top-tools">
    <svg width="14" height="14" viewBox="0 0 14 14" fill="none" stroke="#fff" stroke-width="2"><circle cx="6" cy="6" r="4.5"/><path d="M9.5 9.5L13 13"/></svg>
    <div class="user"><span class="avatar"></span><span>Welcome<br>Mr. Jhon Doe</span></div>
    <svg width="16" height="12" viewBox="0 0 16 12" fill="#fff"><rect width="16" height="2"/><rect y="5" width="16" height="2"/><rect y="10" width="16" height="2"/></svg>
  </div>
</header>

<section class="hero">
  <div class="hero-stage photo" role="img" aria-label="Two doctors in white coats talking at a table in a bright city office"></div>
  <div class="hero-tab">Latest TV Show</div>
  <div class="hero-caption">
    <h1>MR. JHON DOE</h1>
    <p>Weekly field medicine stories from the trail and the studio.</p>
  </div>
  <div class="hero-dots"><span class="on"></span><span></span><span></span><span></span></div>

  <aside class="favorites">
    <h3>Favorite Shows</h3>
    <div class="fav-item"><div class="fav-thumb photo" role="img" aria-label="Show still of a doctor interview"></div><div class="fav-text"><b>Night Rescue Drill</b><small>Season 2 · 24 min</small></div></div>
    <div class="fav-item"><div class="fav-thumb photo" role="img" aria-label="Show still of a field clinic"></div><div class="fav-text"><b>High Altitude Care</b><small>Season 2 · 31 min</small></div></div>
    <div class="fav-item"><div class="fav-thumb photo" role="img" aria-label="Show still of a studio panel"></div><div class="fav-text"><b>Snakebite Myths</b><small>Season 1 · 22 min</small></div></div>
    <div class="fav-item"><div class="fav-thumb photo" role="img" aria-label="Show still of a rescue team"></div><div class="fav-text"><b>Cold Water Survival</b><small>Season 1 · 27 min</small></div></div>
    <div class="fav-item"><div class="fav-thumb photo" role="img" aria-label="Show still of a medic briefing"></div><div class="fav-text"><b>Backcountry Triage</b><small>Season 1 · 25 min</small></div></div>
  </aside>
</section>

<aside class="sidebar">
  <ul class="side-menu">
    <li class="head">Shows</li>
    <li>Latest Upload</li>
    <li>Popular Upload</li>
    <li>Preview</li>
    <li>Recaps</li>
    <li>Classic Shows</li>
  </ul>
  <div class="side-list">
    <div class="label">In the media</div>
    <div class="side-entry"><b>The standard Lorem Ipsum</b><p>Sed ut perspiciatis unde omnis iste natus error sit.</p></div>
    <div class="side-entry"><b>The standard Lorem Ipsum</b><p>Sed ut perspiciatis unde omnis iste natus error sit.</p></div>
    <div class="side-entry"><b>The standard Lorem Ipsum</b><p>Sed ut perspiciatis unde omnis iste natus error sit.</p></div>
    <div class="side-entry"><b>The standard Lorem Ipsum</b><p>Sed ut perspiciatis unde omnis iste natus error sit.</p></div>
    <div class="side-entry"><b>The standard Lorem Ipsum</b><p>Sed ut perspiciatis unde omnis iste natus error sit.</p></div>
  </div>
</aside>

<section class="popular">
  <div class="section-head">
    <h2><b>POPULAR</b> SHOW (35)</h2>
    <div class="filter"><span class="select">Last Week ▾</span>
      <svg width="14" height="12" viewBox="0 0 14 12" fill="#999"><rect width="14" height="2"/><rect y="5" width="14" height="2"/><rect y="10" width="14" height="2"/></svg>
      <svg width="12" height="12" viewBox="0 0 12 12" fill="#999"><rect width="5" height="5"/><rect x="7" width="5" height="5"/><rect y="7" width="5" height="5"/><rect x="7" y="7" width="5" height="5"/></svg>
    </div>
  </div>
  <div class="grid">
    <article class="card"><div class="thumb photo" role="img" aria-label="Two doctors in conversation"></div><h4>The Last Month Of particular</h4><p>Sed ut perspiciatis unde omnis iste</p><div class="meta"><span><i>●</i> 4,872</span><span>Watched</span></div></article>
    <article class="card"><div class="thumb photo" role="img" aria-label="Two doctors in conversation"></div><h4>The Last Month Of particular</h4><p>Sed ut perspiciatis unde omnis iste</p><div class="meta"><span><i>●</i> 4,872</span><span>Watched</span></div></article>
    <article class="card"><div class="thumb photo" role="img" aria-label="Two doctors in conversation"></div><h4>The Last Month Of particular</h4><p>Sed ut perspiciatis unde omnis iste</p><div class="meta"><span><i>●</i> 4,872</span><span>Watched</span></div></article>
    <article class="card"><div class="thumb photo" role="img" aria-label="Two doctors in conversation"></div><h4>The Last Month Of particular</h4><p>Sed ut perspiciatis unde omnis iste</p><div class="meta"><span><i>●</i> 4,872</span><span>Watched</span></div></article>
    <article class="card"><div class="thumb photo" role="img" aria-label="Two doctors in conversation"></div><h4>The Last Month Of particular</h4><p>Sed ut perspiciatis unde omnis iste</p><div class="meta"><span><i>●</i> 4,872</span><span>Watched</span></div></article>
    <article class="card"><div class="thumb photo" role="img" aria-label="Two doctors in conversation"></div><h4>The Last Month Of particular</h4><p>Sed ut perspiciatis unde omnis iste</p><div class="meta"><span><i>●</i> 4,872</span><span>Watched</span></div></article>
    <article class="card"><div class="thumb photo" role="img" aria-label="Two doctors in conversation"></div><h4>The Last Month Of particular</h4><p>Sed ut perspiciatis unde omnis iste</p><div class="meta"><span><i>●</i> 4,872</span><span>Watched</span></div></article>
    <article class="card"><div class="thumb photo" role="img" aria-label="Two doctors in conversation"></div><h4>The Last Month Of particular</h4><p>Sed ut perspiciatis unde omnis iste</p><div class="meta"><span><i>●</i> 4,872</span><span>Watched</span></div></article>
  </div>
</section>

<section class="interview">
  <div class="interview-photo photo" role="img" aria-label="Two doctors seated at a desk during an interview"></div>
  <div class="interview-copy">
    <h2>MR. JHON DOE</h2>
    <h3>Interview</h3>
    <p>A candid talk about life as a wilderness physician, the lessons learned in the field and how the show brings emergency care skills to everyone at home.</p>
    <a href="#" class="btn">READ MORE</a>
  </div>
</section>

<section class="lower">
  <div class="lecture">
    <div class="col-head"><h2>LECTURE</h2><p>The standard Lorem Ipsum passage</p></div>
    <div class="lec-grid">
      <article class="lec"><div class="thumb photo" role="img" aria-label="Lecture hall audience"></div><div class="stars">★★★★★</div><h4>Sed ut perspiciatis unde omnis iste natus</h4><p>Field trauma course review from paramedic students this spring.</p></article>
      <article class="lec"><div class="thumb photo" role="img" aria-label="Speaker at a conference"></div><div class="stars">★★★★★</div><h4>Sed ut perspiciatis unde omnis iste natus</h4><p>Keynote notes on altitude illness for rescue team leaders.</p></article>
      <article class="lec"><div class="thumb photo" role="img" aria-label="Workshop group at tables"></div><div class="stars">★★★★★</div><h4>Sed ut perspiciatis unde omnis iste natus</h4><p>Hands-on splinting workshop feedback from nursing residents.</p></article>
      <article class="lec"><div class="thumb photo" role="img" aria-label="Seminar with a presenter"></div><div class="stars">★★★★★</div><h4>Sed ut perspiciatis unde omnis iste natus</h4><p>Grand rounds summary on remote medicine and evacuation plans.</p></article>
    </div>
  </div>
  <div class="news">
    <div class="col-head"><h2>NEWS</h2><p>The standard Lorem Ipsum passage</p></div>
    <div class="news-item"><div class="news-thumb photo" role="img" aria-label="News photo"></div><div><b>Sed ut perspiciatis unde omnis iste natus</b><p>Local paper covers the new season and the rescue stories behind it.</p></div></div>
    <div class="news-item"><div class="news-thumb photo" role="img" aria-label="News photo"></div><div><b>Sed ut perspiciatis unde omnis iste natus</b><p>Magazine feature on training volunteers for mountain emergencies.</p></div></div>
    <div class="news-item"><div class="news-thumb photo" role="img" aria-label="News photo"></div><div><b>Sed ut perspiciatis unde omnis iste natus</b><p>Radio interview on safe hiking habits for families this summer.</p></div></div>
    <div class="news-item"><div class="news-thumb photo" role="img" aria-label="News photo"></div><div><b>Sed ut perspiciatis unde omnis iste natus</b><p>Journal article on field research into cold injury treatment.</p></div></div>
    <div class="news-item"><div class="news-thumb photo" role="img" aria-label="News photo"></div><div><b>Sed ut perspiciatis unde omnis iste natus</b><p>Award announced for outstanding service in rural emergency care.</p></div></div>
  </div>
</section>

<footer class="footer">
  <div class="social"><span></span><span></span><span></span></div>
  <p class="copy">Copyright © 2024 <b>Trailside MD</b>. All Rights Reserved.</p>
</footer>

</body>
</html>
```